Maple & Quill Week

create an 81/2 x 11 2-sided color flyer
Front cover should have musical artistry theme and health
Front cover should also identify Tembrava exhibit being showcased
The back page should highlight featured performers and the artists’ bio

Target Market(s)

Families, and millennials

Industry/Entity Type

Museum

Font styles to use
Sans Serif

Colors

Designer to choose colors to be used in the design.

Requirements
Must have
• Eye-popping front cover that conveys music, health and Spring Break at The Larkfield Museum

```html
<!DOCTYPE html>
<html lang="en">
<head>
<meta charset="utf-8">
<title>Maple &amp; Quill Week – Flyer</title>
<link href="https://fonts.googleapis.com/css2?family=Rubik:wght@400;500;700;900&family=Open+Sans:wght@400;600&display=swap" rel="stylesheet">
<style>
:root{
  --bg:#7a7a7a;
  --paper:#ffffff;
  --frame:#c9c9c9;
  --green:#78b51f;
  --red:#e8400f;
  --blue:#1aa3e8;
  --orange:#f0a11b;
  --ink:#2b2b2b;
  --body:#333333;
  --yellow:#f7b416;
}
*{margin:0;padding:0;box-sizing:border-box}
html,body{width:1200px;height:1200px;overflow:hidden;background:var(--bg)}
.canvas{position:relative;width:1200px;height:1200px}
.page{position:absolute;top:248px;width:547px;height:703px;background:var(--paper);box-shadow:0 4px 10px rgba(0,0,0,.35)}
.front{left:37px}
.back{left:617px;font-family:"Open Sans",sans-serif}

/* front */
.front-frame{position:absolute;inset:14px;border:2px solid var(--frame)}
.brand{font-family:"Rubik",sans-serif;font-weight:400;color:var(--blue);white-space:nowrap}
.front .brand{position:absolute;top:24px;left:0;right:0;text-align:center;font-size:32px;letter-spacing:-.5px}
.hero-art{position:absolute;left:88px;top:128px;width:372px;height:252px;border-radius:46% 46% 40% 40%;
  background:radial-gradient(ellipse at 50% 55%,#f6c21c 0,#e8561a 30%,#3aa4d8 58%,rgba(120,181,31,.55) 72%,rgba(255,255,255,0) 76%)}
.event-title{position:absolute;left:0;right:0;text-align:center;font-family:"Rubik",sans-serif;font-weight:900;line-height:1}
.t-green{top:404px;font-size:54px;color:var(--green)}
.t-red{top:456px;font-size:54px;color:var(--red)}
.t-week{top:512px;font-size:44px;font-weight:500;color:var(--ink);letter-spacing:1px}
.date-rule{position:absolute;left:120px;width:306px;height:2px;background:var(--ink)}
.date-line{position:absolute;left:0;right:0;top:582px;text-align:center;font-family:"Rubik",sans-serif;font-weight:900;font-size:36px;color:var(--ink);line-height:1}
.date-line .range{color:var(--green)}
.date-line sup{font-size:19px;vertical-align:15px}
.url{position:absolute;left:0;right:0;top:652px;text-align:center;font-family:"Open Sans",sans-serif;font-size:14.5px;letter-spacing:2px;color:var(--ink)}

/* back */
.live{position:absolute;left:31px;top:10px;font-family:"Rubik",sans-serif;font-weight:900;font-size:60px;line-height:1;color:var(--red);letter-spacing:-1px}
.performance{position:absolute;left:31px;top:64px;font-family:"Rubik",sans-serif;font-weight:700;font-size:30px;line-height:1;color:var(--red)}
.butterflies{position:absolute;left:190px;top:4px;width:58px;height:52px;border-radius:50%;background:radial-gradient(circle,#f6b21c 0,#e8561a 40%,rgba(58,164,216,.4) 62%,rgba(255,255,255,0) 70%)}
.back .brand{position:absolute;left:292px;top:16px;font-size:18px}
.day{font-family:"Rubik",sans-serif;font-weight:700;color:var(--blue);font-size:16.5px;line-height:1}
.act{font-family:"Rubik",sans-serif;font-weight:700;color:var(--orange);font-size:12px;line-height:1.15;margin:10px 0 6px}
.bio{font-size:9.4px;line-height:11.8px;color:var(--body);text-align:justify}
.col-right{position:absolute;left:291px;top:76px;width:234px}
.col-right .day{margin-bottom:8px}
.wed-box{position:absolute;left:23px;top:134px;width:243px;height:210px;border:1px solid var(--ink);border-top:none;padding:10px 12px 0 14px}
.wed-box::before,.wed-box::after{content:"";position:absolute;top:0;height:1px;background:var(--ink)}
.wed-box::before{left:0;width:14px}
.wed-box::after{right:0;width:14px}
.wed-box .day{position:absolute;top:-8px;left:21px;padding:0 5px;background:var(--paper)}
.wed-box .act:first-of-type{margin-top:12px}
.fri-band{position:absolute;left:0;top:368px;width:547px;height:88px;background:var(--green)}
.fri-tab{position:absolute;left:24px;top:0;background:var(--paper);padding:4px 9px 5px}
.fri-col{position:absolute;top:34px;width:215px}
.fri-col.left{left:27px;top:32px}
.fri-col.right{left:296px;top:12px}
.fri-band .act{color:#fff;margin:0 0 5px}
.fri-band .bio{color:#fff}
.divider{position:absolute;left:273px;top:12px;width:1px;height:70px;background:#3f6a12}
.sat{position:absolute;left:25px;top:480px;width:500px}
.sat .act{margin-top:9px}
.bottom-bar{position:absolute;left:0;bottom:0;width:547px;height:6px;background:var(--yellow)}
</style>
</head>
<body>
<div class="canvas">

  <section class="page front">
    <div class="front-frame"></div>
    <div class="brand">The Larkfield Museum</div>
    <div class="hero-art" role="img" aria-label="Colourful illustration of a brain wearing headphones surrounded by musical notes, hearts and medical crosses"></div>
    <div class="event-title t-green">MAPLE &amp;</div>
    <div class="event-title t-red">QUILL</div>
    <div class="event-title t-week">WEEK</div>
    <div class="date-rule" style="top:570px"></div>
    <div class="date-line"><span class="range">12<sup>th</sup>-17<sup>th</sup></span> MARCH</div>
    <div class="date-rule" style="top:626px"></div>
    <div class="url">www.larkfieldmuseum.org</div>
  </section>

  <section class="page back">
    <div class="live">LIVE</div>
    <div class="butterflies" role="img" aria-label="Colourful butterflies and musical notes"></div>
    <div class="performance">PERFORMANCE</div>
    <div class="brand">The Larkfield Museum</div>

    <div class="wed-box">
      <div class="day">WEDNESDAY, MARCH 14</div>
      <div class="act">3pm - Dorian Vale</div>
      <p class="bio">Dorian Vale is a Baytown native Alternative Hip Hop artist; his sound is a blend of smooth hip hop with off kilter rhymes that redirect you to the movie scene in your ears.</p>
      <div class="act">4pm - Kasimo Verse</div>
      <p class="bio">One of the Bayline Weekly 2017 Top Ten Acts to Watch, Kasimo Verse is doing Rap his own way. For years, he has been cutting his teeth playing house shows, organizing events, and opening for touring acts. His proven skill set and pertinent lyrics have him alongside some of Houston's most prominent rap acts.</p>
    </div>

    <div class="col-right">
      <div class="day">THURSDAY, MARCH 15</div>
      <div class="act">3pm-Marisa Joy Hollis</div>
      <p class="bio">As a contestant on Stage Search in 2012, Marisa Joy Hollis has wowed crowds across America. A Houston native, she is known to melt hearts to plasma!</p>
      <div class="act">Nora Castel</div>
      <p class="bio">Nora Castel is a local self-taught visual artist. She also dabbles in creating music and poetry. Typically, her music and art consists of themes tied to beauty and pain often with a dramatic flourishing duality.</p>
      <div class="act">4pm-Quenn &amp; Neon Soul Society</div>
      <p class="bio">Quenn is an electronic soul singer and flamboyant performer whose sound is a blend of dancey, house rhythms &amp; church tinged vocals. In 2014, he became background vocalist for Harbor Soul originators, The Lanterns and is currently finishing up his debut EP due out before summer.</p>
    </div>

    <div class="fri-band">
      <div class="fri-tab day">FRIDAY, MARCH 16</div>
      <div class="fri-col left">
        <div class="act">3pm- Remy Solano</div>
        <p class="bio">Remy Solano is an experimental/techno music producer from Houston, TX.</p>
      </div>
      <div class="divider"></div>
      <div class="fri-col right">
        <div class="act">4pm - Vexx</div>
        <p class="bio">Vexx is a Houston based DJ/producer. He is signed with the Cobalt label. Vexx also goes by Night Tide - who throws the Low Hum and Exhibition parties.</p>
      </div>
    </div>

    <div class="sat">
      <div class="day">SATURDAY MARCH 17TH</div>
      <div class="act">3pm-Juno Sparrow</div>
      <p class="bio">Juno Sparrow has been building a team of Art Queens since the day she was born. Her goal is to inspire others to be brave about pursuing art as a career by becoming a living example. She continues the Creations with her Gift of Song by writing and singing with fellow artists around Houston. Check out her Album on Streamwave or Tunefold “Open Doors” to get a taste of what's she done and what's to come!</p>
      <div class="act">3:45pm- Pallor</div>
      <p class="bio">LA-based visual artist and musician, Elias Brandt began releasing music as Pallor in the Summer of 2013. Drawing on artists such as Vesna, Hollowfield, and Ada Ren, he crafted an idiosyncratic style that fell gracefully between folk, gospel, and experimental electronic music. By 2014, he had released his debut EP, Still Waters. In 2015, he released his second EP, Driftwood. In 2017, he self-released an EP entitled quiet, just ash, a 5-song collection exploring language, loss, and identity through ambient-noise soundscapes. Brandt donated half of all proceeds from the release to Riverbend Collective, who have provided legal support to water protectors since the founding of the Cedar Ridge Camp. He is currently working on his debut full-length release.</p>
    </div>

    <div class="bottom-bar"></div>
  </section>

</div>
</body>
</html>
```